We have built a site at brightgadgetnotes.net, but it is missing several elements and several don't work. I even like the color scheme we have. I do not know to do too much with code so if there is anything I need to do, it must be very minimal.

We essentially want what is there with:

1) a small column on the left side for categories, which are currently bottom right
2) space for a 728-90 banner ad at the top under the menu below the logo
3) drop down menus under the top logo that actually work
4) the top menu (where we have ages), the logo, the drop down menus and the 728-90 banner all need to space together neatly
5) the top logo needs to center
6) under the title of each post on the home page it says "comment and reactions." I'd like reactions removed since I have no idea what they are.
7) must be able to accept all widgets
8) I need a simple way to access the code to the top banner ad when it is placed to change as needed

That's about it other than any suggestions to make it better. I like clean and simple in blog format.
Updates

Sorry I should have mentioned that we want the text of the categories smaller so that can fit in a smaller left column. I'd have to see but I'd guess about 10 point.

Industry/Entity Type

Work

Requirements
Must have
• see above

```html
<!DOCTYPE html>
<html lang="en">
<head>
<meta charset="utf-8">
<title>Bright Gadget Notes</title>
<link rel="stylesheet" href="https://fonts.googleapis.com/css2?family=Montserrat:wght@500;600;700&family=Open+Sans:ital,wght@0,400;0,600;0,700;1,700&display=swap">
<style>
:root{
  --gold:#e9b52a;
  --gold-dark:#d59e12;
  --gold-bar:#c8900c;
  --footer:#e1a80e;
  --ink:#1f1f1f;
  --text:#6b6b6b;
  --muted:#8a8a8a;
  --orange:#e8730f;
  --green:#4f9a12;
  --green-light:#7cc227;
  --line:#e4e4e4;
  --frame:#e9e9e9;
  --dark:#2b2b2b;
}
*{box-sizing:border-box;margin:0;padding:0}
html,body{width:1200px;height:2191px;overflow:hidden}
body{position:relative;background:#fff;font-family:"Open Sans",Arial,sans-serif;color:var(--text)}
.header{position:absolute;left:0;top:0;width:1200px;height:345px;
  background:linear-gradient(180deg,var(--gold) 0%,var(--gold) 68%,#f3d98d 85%,#fff 100%)}
.age-bar{position:absolute;left:0;top:0;width:1200px;height:26px;background:var(--gold-bar);
  display:flex;justify-content:center;gap:28px;align-items:center}
.age-bar a{color:#fff;font:600 13px "Open Sans",sans-serif;text-decoration:none;letter-spacing:.3px}
.brand{position:absolute;left:200px;top:40px;width:805px;height:100px;display:flex;align-items:center;justify-content:center;gap:18px}
.brand-mark{width:44px;height:44px;border-radius:50%;background:#3b2c12}
.brand-name{font:700 52px "Montserrat",sans-serif;color:#3b2c12;text-transform:uppercase;letter-spacing:1px;white-space:nowrap}
.search{position:absolute;left:140px;top:159px;width:218px;height:29px;display:flex}
.search input,.signup input{flex:1;min-width:0;border:0;background:#fff;padding:0 10px;font:11px "Open Sans",sans-serif;color:#999}
.search button{width:34px;border:0;background:var(--dark);display:flex;align-items:center;justify-content:center}
.alert-box{position:absolute;left:140px;top:208px;width:218px}
.alert-box h2{font:500 23px "Montserrat",sans-serif;color:#2a1e05;white-space:nowrap}
.alert-box p{font:12px "Open Sans",sans-serif;color:#3a2a05;margin-top:6px;white-space:nowrap}
.signup{display:flex;height:29px;margin-top:9px}
.signup button{width:58px;border:0;background:var(--green-light);color:#fff;font:700 13px "Open Sans",sans-serif}
.ad-banner{position:absolute;left:377px;top:159px;width:683px;height:84px;background:#f7f4ec;border:2px solid #f1e3b8;
  display:flex;align-items:center;padding:0 24px;gap:32px}
.ad-name{font:600 34px "Open Sans",sans-serif;color:#3b3b3b}
.ad-art{flex:1;height:56px;background:linear-gradient(90deg,#e4e0d6,#f0ebe0 50%,#e4e0d6)}
.main-nav{position:absolute;left:377px;top:263px;width:683px;height:33px;display:flex;
  background:linear-gradient(180deg,var(--green-light),var(--green))}
.main-nav a{flex:1;text-align:center;line-height:33px;color:#fff;font:italic 700 15px "Open Sans",sans-serif;text-decoration:none;border-right:1px solid #5da11a}
.main-nav a:first-child{background:linear-gradient(180deg,#5a9b16,#3f7d0b)}
.main-nav a:last-child{border-right:0}
.sidebar{position:absolute;left:140px;top:343px;width:216px}
.widget-title{position:relative;height:40px;background:var(--dark);color:#fff;font:600 16px "Montserrat",sans-serif;
  line-height:40px;padding-left:30px;text-transform:uppercase;letter-spacing:.3px;width:216px;
  clip-path:polygon(0 0,96% 0,100% 100%,0 100%)}
.widget-title::before{content:"";position:absolute;left:0;top:0;width:16px;height:40px;background:var(--green)}
.widget-title::after{content:"";position:absolute;left:5px;top:14px;border:6px solid transparent;border-left:7px solid #fff}
.dev-text{font:12px/1.6 "Open Sans",sans-serif;color:#333;padding:10px 0 0;word-break:break-all}
.cat-box{margin-top:2px;border:1px solid var(--line);border-top:0;padding:10px 0 22px 14px}
.cat-list{list-style:none}
.cat-list li{font:11px/23.4px "Open Sans",sans-serif;color:var(--muted);white-space:nowrap}
.cat-list li.active{color:#d02a1a}
.post{position:absolute;left:385px;width:675px}
.post h2{font:600 21px "Montserrat",sans-serif;color:var(--ink);height:38px;white-space:nowrap}
.post-figure{position:absolute;left:0;top:38px;width:553px;height:267px;border:5px solid var(--frame)}
.post-figure div{width:100%;height:100%}
.meta{position:absolute;left:561px;top:38px;width:114px}
.date{height:28px;background:var(--orange);color:#fff;font:700 12px/28px "Open Sans",sans-serif;text-align:center;white-space:nowrap}
.meta-row{display:flex;align-items:center;gap:7px;height:36px;font:11px "Open Sans",sans-serif;color:#555;border-bottom:1px solid #f0f0f0;padding-left:8px;white-space:nowrap}
.meta-row span{white-space:nowrap}
.meta-row b{color:#222}
.meta-gap{height:50px;border-bottom:1px solid #f0f0f0}
.ico{width:10px;height:10px;flex:none}
.share{width:10px;height:10px;border-radius:50%;background:#4a9fe0;flex:none}
.excerpt{position:absolute;left:0;top:324px;width:675px;font:12px/19px "Open Sans",sans-serif;color:var(--text)}
.excerpt a{color:var(--orange);font-size:11px;text-decoration:none;white-space:nowrap}
.divider{position:absolute;left:0;top:406px;width:675px;height:1px;background:var(--line)}
.footer{position:absolute;left:0;top:2136px;width:1200px;height:55px;background:var(--footer)}
.footer-links{position:absolute;left:140px;top:10px;font:700 12px "Open Sans",sans-serif;color:#fff}
.footer-links span{margin:0 6px}
.copyright{position:absolute;left:140px;top:30px;font:10.5px "Open Sans",sans-serif;color:#7a5600}
.social{position:absolute;left:956px;top:14px;display:flex;gap:12px}
.social i{width:26px;height:26px;border-radius:50%;background:#fff;display:block}
</style>
</head>
<body>
<header class="header">
  <nav class="age-bar">
    <a href="#">AGES 1-2 (TODDLER)</a><a href="#">AGES 3-4 (PRE SCHOOL)</a><a href="#">AGES 5-6</a><a href="#">AGES 7-8</a><a href="#">AGES 9-10</a>
  </nav>
  <div class="brand"><span class="brand-mark"></span><span class="brand-name">Bright Gadget Notes</span></div>
  <form class="search"><input type="text" value="Search" aria-label="Search"><button type="button" aria-label="Search">
    <svg width="16" height="16" viewBox="0 0 16 16"><circle cx="6.5" cy="6.5" r="4.5" fill="none" stroke="#fff" stroke-width="2"/><line x1="10" y1="10" x2="14.5" y2="14.5" stroke="#fff" stroke-width="2.4"/></svg>
  </button></form>
  <div class="alert-box">
    <h2>Gadget App Alert</h2>
    <p>Subscribe to our Gadget App Alert!</p>
    <form class="signup"><input type="text" value="Email" aria-label="Email"><button type="button">Sign up</button></form>
  </div>
  <div class="ad-banner">
    <span class="ad-name">Iconvale</span>
    <div class="ad-art" role="img" aria-label="Advertising banner with a row of app icons"></div>
  </div>
  <nav class="main-nav"><a href="#">Best Free Apps</a><a href="#">Free Apps</a><a href="#">Best Apps</a><a href="#">Submit App</a></nav>
</header>

<aside class="sidebar">
  <h3 class="widget-title">Developers</h3>
  <p class="dev-text">Send us your app info!<br>http://www.brightgadgetkids.com/<br>welcome-gadget-developers.html</p>
  <h3 class="widget-title" style="margin-top:30px">App Categories</h3>
  <div class="cat-box">
    <ul class="cat-list">
      <li class="active">Addition (2)</li><li>Ages 1-2 (toddler) (2)</li><li>Ages 3-4 (preschool) (9)</li><li>Ages 5-6 (7)</li><li>Ages 7-8 (2)</li><li>Ages 8-9 (1)</li><li>Ages 9-10 (2)</li><li>Alphabet/letters (3)</li><li>Animals (1)</li><li>Art (2)</li><li>Best apps (3)</li><li>Best free apps (2)</li><li>Books (1)</li><li>Coloring (1)</li><li>Colors (1)</li><li>Connect the dots (1)</li><li>Drawing (1)</li><li>Engineering (1)</li><li>English (1)</li><li>Food and drink (1)</li><li>Free apps (4)</li><li>Hand-eye coordination (2)</li><li>Has in-app purchases (2)</li><li>Has third-party ads (1)</li><li>Health (1)</li><li>Just for fun (1)</li><li>Matching (2)</li><li>Math (3)</li><li>Mazes (1)</li><li>Music (1)</li><li>Numbers/counting (3)</li><li>Patterns (2)</li><li>Phonics (1)</li><li>Puzzles (1)</li><li>Reading, sentences (1)</li><li>Reading, words (1)</li><li>Role-playing (1)</li><li>Science (1)</li><li>Social studies (1)</li><li>Sorting (1)</li><li>Subtraction (2)</li><li>Tech (1)</li><li>Uncategorized (5)</li>
    </ul>
  </div>
</aside>

<main>
  <article class="post" style="top:349px">
    <h2>Proin gravida nibh vel velit auctor aliquet.</h2>
    <figure class="post-figure"><div role="img" aria-label="App screenshot of a letter names and letter sounds progress tracker" style="background:linear-gradient(135deg,#e23a2c,#f4f4f4 55%,#d8302a)"></div></figure>
    <div class="meta">
      <div class="date">21 APR 2013</div>
      <div class="meta-row"><svg class="ico" viewBox="0 0 10 10"><path d="M0 0h10v7H4L1 10V7H0z" fill="#e8730f"/></svg><span>Comment (<b>10</b>)</span></div>
      <div class="meta-row"><svg class="ico" viewBox="0 0 10 10"><circle cx="5" cy="3" r="2.5" fill="#e8730f"/><path d="M0 10a5 4 0 0 1 10 0z" fill="#e8730f"/></svg><span>Admin</span></div>
      <div class="meta-gap"></div>
      <div class="meta-row"><i class="share"></i><span>Chirper</span></div>
      <div class="meta-row"><i class="share" style="background:#3b5b98"></i><span>Friendbook</span></div>
      <div class="meta-row"><i class="share" style="background:#1a7bb9"></i><span>Worknet</span></div>
    </div>
    <p class="excerpt">Lorem Ipsum. Proin gravida nibh vel velit auctor aliquet. Aenean sollicitudin, lorem quis bibendum auctor, nisi elit consequat ipsum, sagittis sem nibh id elit. Duis sed odio sit amet nibh vulputate cursus a sit amet mauris. Morbi accumsan ipsum velit. Nam nec tellus a odio tincidunt...... <a href="#">[Read More]</a></p>
    <div class="divider"></div>
  </article>

  <article class="post" style="top:792px">
    <h2>Morbi accumsan ipsum velit.</h2>
    <figure class="post-figure"><div role="img" aria-label="App screenshots of an underwater letter game and a letter safari game" style="background:linear-gradient(135deg,#5cc6e8,#f2c84a 55%,#3a8fd0)"></div></figure>
    <div class="meta">
      <div class="date">21 APR 2013</div>
      <div class="meta-row"><svg class="ico" viewBox="0 0 10 10"><path d="M0 0h10v7H4L1 10V7H0z" fill="#e8730f"/></svg><span>Comment (<b>10</b>)</span></div>
      <div class="meta-row"><svg class="ico" viewBox="0 0 10 10"><circle cx="5" cy="3" r="2.5" fill="#e8730f"/><path d="M0 10a5 4 0 0 1 10 0z" fill="#e8730f"/></svg><span>Admin</span></div>
      <div class="meta-gap"></div>
      <div class="meta-row"><i class="share"></i><span>Chirper</span></div>
      <div class="meta-row"><i class="share" style="background:#3b5b98"></i><span>Friendbook</span></div>
      <div class="meta-row"><i class="share" style="background:#1a7bb9"></i><span>Worknet</span></div>
    </div>
    <p class="excerpt">Lorem Ipsum. Proin gravida nibh vel velit auctor aliquet. Aenean sollicitudin, lorem quis bibendum auctor, nisi elit consequat ipsum, sagittis sem nibh id elit. Duis sed odio sit amet nibh vulputate cursus a sit amet mauris. Morbi accumsan ipsum velit........<a href="#">[Read More]</a></p>
    <div class="divider"></div>
  </article>

  <article class="post" style="top:1236px">
    <h2>Aenean sollicitudin, lorem quis bibendum auctor.</h2>
    <figure class="post-figure"><div role="img" aria-label="App screenshots of a golden letter tracing game and a world map game" style="background:linear-gradient(135deg,#f3b433,#7cc0e0 55%,#e9a13a)"></div></figure>
    <div class="meta">
      <div class="date">21 APR 2013</div>
      <div class="meta-row"><svg class="ico" viewBox="0 0 10 10"><path d="M0 0h10v7H4L1 10V7H0z" fill="#e8730f"/></svg><span>Comment (<b>10</b>)</span></div>
      <div class="meta-row"><svg class="ico" viewBox="0 0 10 10"><circle cx="5" cy="3" r="2.5" fill="#e8730f"/><path d="M0 10a5 4 0 0 1 10 0z" fill="#e8730f"/></svg><span>Admin</span></div>
      <div class="meta-gap"></div>
      <div class="meta-row"><i class="share"></i><span>Chirper</span></div>
      <div class="meta-row"><i class="share" style="background:#3b5b98"></i><span>Friendbook</span></div>
      <div class="meta-row"><i class="share" style="background:#1a7bb9"></i><span>Worknet</span></div>
    </div>
    <p class="excerpt">Lorem Ipsum. Proin gravida nibh vel velit auctor aliquet. Aenean sollicitudin, lorem quis bibendum auctor, nisi elit consequat ipsum, sagittis sem nibh id elit. Duis sed odio sit amet nibh vulputate cursus a sit amet mauris. Morbi accumsan ipsum velit. Nam nec tellus a odio tincidunt....... <a href="#">[Read More]</a></p>
    <div class="divider"></div>
  </article>

  <article class="post" style="top:1680px">
    <h2>Proin gravida nibh vel velit auctor aliquet.</h2>
    <figure class="post-figure"><div role="img" aria-label="App screenshots of an underwater letter game and a letter safari game" style="background:linear-gradient(135deg,#5cc6e8,#f2c84a 55%,#3a8fd0)"></div></figure>
    <div class="meta">
      <div class="date">21 APR 2013</div>
      <div class="meta-row"><svg class="ico" viewBox="0 0 10 10"><path d="M0 0h10v7H4L1 10V7H0z" fill="#e8730f"/></svg><span>Comment (<b>10</b>)</span></div>
      <div class="meta-row"><svg class="ico" viewBox="0 0 10 10"><circle cx="5" cy="3" r="2.5" fill="#e8730f"/><path d="M0 10a5 4 0 0 1 10 0z" fill="#e8730f"/></svg><span>Admin</span></div>
      <div class="meta-gap"></div>
      <div class="meta-row"><i class="share"></i><span>Chirper</span></div>
      <div class="meta-row"><i class="share" style="background:#3b5b98"></i><span>Friendbook</span></div>
      <div class="meta-row"><i class="share" style="background:#1a7bb9"></i><span>Worknet</span></div>
    </div>
    <p class="excerpt">Lorem Ipsum. Proin gravida nibh vel velit auctor aliquet. Aenean sollicitudin, lorem quis bibendum auctor, nisi elit consequat ipsum, sagittis sem nibh id elit. Duis sed odio sit amet nibh vulputate cursus a sit amet mauris......... <a href="#">[Read More]</a></p>
    <div class="divider"></div>
  </article>
</main>

<footer class="footer">
  <div class="footer-links">Best Free Apps<span>|</span>Free Apps<span>|</span>Best Apps<span>|</span>Submit App</div>
  <div class="copyright">© 2013 Bright Gadget Notes. All Rights Reserved | Privacy Statement</div>
  <div class="social"><i></i><i></i><i></i></div>
</footer>
</body>
</html>
```